Cosmetic retail chain developes private label products. We need package designe for creme soap.

We need package designe for bar creme soap in cardboard package. Benchmark is Tulk. The name of our private label for this product is Nerisa.

```html
<!DOCTYPE html>
<html lang="en">
<head>
<meta charset="utf-8">
<title>Nerisa Bar Creme Soap – Pack Front</title>
<link href="https://fonts.googleapis.com/css2?family=Cabin:wght@500;600;700&display=swap" rel="stylesheet">
<style>
  :root {
    --bg: #ffffff;
    --pack-light: #f7fbfe;
    --pack-blue: #cfe6f3;
    --navy: #1f1f6b;
    --brand-purple: #3e3a8e;
    --pink: #cc5a9e;
    --pink-light: #e59ac4;
    --green-dark: #5e9a44;
    --green-light: #a9d27a;
  }
  * { margin: 0; padding: 0; box-sizing: border-box; }
  html, body { width: 1196px; height: 1200px; overflow: hidden; background: var(--bg); }
  body { font-family: "Cabin", sans-serif; position: relative; }

  .pack-front {
    position: absolute; left: 60px; top: 250px; width: 1076px; height: 700px;
    border-radius: 34px; overflow: hidden;
    background: linear-gradient(160deg, var(--pack-light) 0%, #eef6fb 45%, var(--pack-blue) 100%);
    box-shadow: 0 6px 22px rgba(60, 90, 120, 0.18);
  }
  .wave-lines { position: absolute; inset: 0; }

  .cream-splash {
    position: absolute; left: 20px; top: 0; width: 520px; height: 520px;
    background: radial-gradient(ellipse at 55% 55%, #ffffff 0%, #f3f6f8 50%, rgba(235, 243, 248, 0) 75%);
  }

  .natural-badge { position: absolute; left: 28px; top: 32px; width: 280px; height: 150px; }
  .natural-badge span {
    position: absolute; color: #fff; font-weight: 500; font-size: 40px; transform: rotate(-10deg);
  }
  .natural-badge .pct { left: 54px; top: 22px; }
  .natural-badge .word { left: 70px; top: 78px; }

  .brand-name {
    position: absolute; left: 545px; top: 100px; width: 440px; text-align: center;
    font-weight: 700; font-size: 150px; line-height: 1; color: var(--brand-purple);
  }

  .product-pill {
    position: absolute; left: 545px; top: 300px; width: 385px; height: 76px;
    border-radius: 38px; background: linear-gradient(180deg, var(--pink-light), var(--pink));
    color: #fff; font-weight: 500; font-size: 44px; line-height: 76px; text-align: center;
  }

  .benefits {
    position: absolute; left: 500px; top: 420px; width: 460px;
    display: flex; justify-content: space-between;
  }
  .benefit { width: 140px; text-align: center; color: var(--navy); font-weight: 600; font-size: 16px; line-height: 1.2; }
  .benefit svg { display: block; margin: 0 auto 6px; width: 60px; height: 56px; }

  .claim-tag {
    position: absolute; left: 92px; top: 560px; padding: 4px 10px;
    background: var(--navy); color: #fff; font-weight: 500; font-size: 31px; line-height: 40px;
  }
  .claim-sub {
    position: absolute; left: 96px; top: 612px;
    color: var(--navy); font-weight: 600; font-size: 23px;
  }
</style>
</head>
<body>
  <div class="pack-front">
    <svg class="wave-lines" viewBox="0 0 1076 700" preserveAspectRatio="none" aria-hidden="true">
      <path d="M0 560 C 400 560, 760 430, 1076 440 L1076 700 L0 700 Z" fill="#bcdcee" opacity="0.35"/>
      <path d="M0 520 C 260 640, 560 640, 1076 480" fill="none" stroke="#ffffff" stroke-width="6" opacity="0.9"/>
      <path d="M0 600 C 300 690, 700 660, 1076 560" fill="none" stroke="#ffffff" stroke-width="4" opacity="0.7"/>
    </svg>

    <div class="cream-splash" role="img" aria-label="Pouring white cream splash"></div>

    <div class="natural-badge">
      <svg width="280" height="150" viewBox="0 0 280 150" aria-hidden="true">
        <path d="M8 6 C 80 20, 150 0, 210 30 L 226 70 C 160 50, 90 80, 30 70 Z" fill="var(--green-dark)"/>
        <path d="M36 86 C 110 80, 170 40, 246 70 L 272 120 C 200 100, 130 140, 56 146 Z" fill="var(--green-light)"/>
      </svg>
      <span class="pct">100%</span>
      <span class="word">Natural</span>
    </div>

    <div class="brand-name">Nerisa</div>

    <div class="product-pill">Bar creme soap</div>

    <div class="benefits">
      <div class="benefit">
        <svg viewBox="0 0 60 56" aria-hidden="true">
          <line x1="42" y1="4" x2="30" y2="28" stroke="var(--navy)" stroke-width="4" stroke-linecap="round"/>
          <path d="M22 26 L38 32 L30 50 L10 44 Z" fill="none" stroke="var(--navy)" stroke-width="3.5" stroke-linejoin="round"/>
          <line x1="18" y1="36" x2="14" y2="44" stroke="var(--navy)" stroke-width="2"/>
          <line x1="26" y1="38" x2="22" y2="47" stroke="var(--navy)" stroke-width="2"/>
        </svg>
        Deep<br>Cleansing
      </div>
      <div class="benefit">
        <svg viewBox="0 0 60 56" aria-hidden="true">
          <circle cx="30" cy="28" r="22" fill="none" stroke="var(--navy)" stroke-width="4"/>
          <circle cx="30" cy="28" r="12" fill="none" stroke="var(--navy)" stroke-width="3"/>
        </svg>
        Promotes<br>Healthy Skin
      </div>
      <div class="benefit">
        <svg viewBox="0 0 60 56" aria-hidden="true">
          <line x1="4" y1="48" x2="56" y2="48" stroke="var(--navy)" stroke-width="4" stroke-linecap="round"/>
          <circle cx="16" cy="40" r="4" fill="var(--navy)"/>
          <circle cx="28" cy="38" r="4" fill="var(--navy)"/>
          <circle cx="40" cy="40" r="4" fill="var(--navy)"/>
          <circle cx="22" cy="28" r="3" fill="var(--navy)"/>
          <circle cx="34" cy="26" r="3" fill="var(--navy)"/>
          <circle cx="28" cy="16" r="2.5" fill="var(--navy)"/>
        </svg>
        Gently Remove<br>Impurities
      </div>
    </div>

    <div class="claim-tag">for soft and smooth skin</div>
    <div class="claim-sub">With 55% Nourishing Moisturizer</div>
  </div>
</body>
</html>
```